National Water and Fire Restoration, Multi Surface Cleaning, Carpet Cleaning Business Needs a Websi

We need a new fresh website for our business. There are multiple services we offer and we need a fresh corporate website that represents us better. We start from cleaning carpet and tiles, to upholstery and curtains, to completely clean all contents and building materials after a fire, or completely dry out a home or business after a major or minor flood event. We are open to all concepts as we want to create a new look, maybe even logo, signage, vehicle signage, uniforms.
We are open to new colours etc.

Go to www.brightlanewashing.com.au for current logo and all other past ideas

Reason: I need to see more quality designs to sink my teeth into

Target Market(s)

The target market is everyone of all walks of life

Industry/Entity Type

Business

Number of Pages Required

3 page

Font styles to use
Sans Serif

Requirements
Must have
• Home page
• Services page
• Contact us page
• The rest is up to your imagination
• ***This is design only - NO CODING REQUIRED***
Nice to have
• Pictures

```html
<!DOCTYPE html>
<html lang="en">
<head>
<meta charset="utf-8">
<title>BrightLane Washing</title>
<link rel="stylesheet" href="https://fonts.googleapis.com/css2?family=Montserrat:wght@400;600;700&family=Open+Sans:wght@400;600&family=Pacifico&family=Oswald:wght@400;500&family=Archivo+Black&display=swap">
<style>
:root{
  --blue:#1a8fd6;
  --blue-dark:#2f6f93;
  --pink:#e5176f;
  --grey-light:#e6e6e8;
  --grey-panel:#ededee;
  --text-dark:#333;
  --text-mid:#777;
  --footer:#474747;
  --footer-deep:#363636;
  --field:#5b5b5b;
  --gold:#e7b734;
}
*{margin:0;padding:0;box-sizing:border-box}
html,body{width:1200px;height:2314px;overflow:hidden}
body{position:relative;font-family:"Open Sans",Arial,sans-serif;color:var(--text-dark);background:#fff}
section,header,footer,nav,div{position:absolute}
.topbar{left:0;top:0;width:1200px;height:41px;background:var(--blue);color:#fff;font-size:13px}
.topbar .util{left:75px;top:12px}
.topbar .social{top:7px;width:26px;height:26px;border-radius:50%;background:#fff}
.topbar .phone{left:878px;top:10px;font-family:Montserrat,sans-serif;font-size:15px;display:flex;align-items:center;gap:6px}
.topbar .schedule{left:1020px;top:9px;width:105px;height:24px;border-radius:5px;background:#fff;color:#222;font-family:Montserrat,sans-serif;font-weight:700;font-size:12px;text-align:center;line-height:24px}
.masthead{left:0;top:41px;width:1200px;height:111px;background:#fff}
.brand{left:75px;top:30px;display:flex;align-items:center;gap:10px;white-space:nowrap}
.brand .dot{width:50px;height:50px;border-radius:50%;background:var(--pink);flex:none}
.brand .name{font-family:Montserrat,sans-serif;font-weight:700;font-size:27px;color:var(--blue)}
.nav{left:468px;top:0;height:111px;display:flex;align-items:center;font-family:Montserrat,sans-serif;font-weight:600;font-size:16px;color:#222;white-space:nowrap}
.nav span.sep{margin:0 10px;color:#555}
.nav .active{position:relative;height:111px;line-height:111px;padding:0 6px;background:linear-gradient(#e6e6e6 0,#f7f7f7 60%,#fff 100%)}
.nav .active::after{content:"";position:absolute;left:6px;right:6px;top:74px;height:3px;background:var(--pink)}
.hero{left:0;top:152px;width:1200px;height:611px;background:linear-gradient(180deg,#b9cbd8 0%,#d9dfe4 40%,#b6aba0 75%,#8e8276 100%)}
.hero .lead{left:73px;top:72px;color:#fff;font-family:Montserrat,sans-serif;font-weight:600;font-size:33px}
.hero .title{left:73px;top:106px;color:var(--pink);font-family:Montserrat,sans-serif;font-weight:700;font-size:56px;letter-spacing:1px}
.reasons{left:73px;top:180px;width:318px}
.reason{position:relative;height:38px;margin-bottom:9px;background:rgba(80,80,80,.75);color:#fff;font-family:Montserrat,sans-serif;font-weight:600;font-size:18px;line-height:38px;padding-left:52px;white-space:nowrap}
.reason::before{content:"";position:absolute;left:10px;top:9px;width:20px;height:20px;border-radius:50%;background:var(--blue)}
.hero .cta{left:104px;top:502px;width:266px;height:48px;background:var(--blue);color:#fff;font-family:Montserrat,sans-serif;font-weight:600;font-size:22px;text-align:center;line-height:48px;border-radius:3px;box-shadow:0 3px 0 #0e6aa3}
.ribbon{left:1042px;top:0;width:74px;height:132px;background:var(--gold);clip-path:polygon(0 0,100% 0,100% 100%,50% 86%,0 100%);text-align:center;color:#3a2a00}
.ribbon .small{position:static;font-size:14px;margin-top:4px}
.ribbon .big{position:static;font-family:Georgia,serif;font-style:italic;font-size:40px;line-height:40px;color:#fff}
.ribbon .tiny{position:static;font-size:8px;line-height:10px;padding:0 5px}
.signup{left:0;top:763px;width:1200px;height:120px;background:var(--grey-light)}
.signup h2{position:absolute;left:0;width:1200px;top:10px;text-align:center;font-family:Montserrat,sans-serif;font-weight:600;font-size:26px;color:#1d1d1d}
.signup .field{left:195px;top:56px;width:490px;height:43px;background:#fff;color:#999;font-size:22px;line-height:43px;padding-left:14px}
.signup .submit{left:705px;top:56px;width:300px;height:43px;background:var(--blue);color:#fff;font-family:Montserrat,sans-serif;font-weight:700;font-size:22px;line-height:43px;text-align:center}
.signup .submit svg{position:absolute;right:12px;top:9px}
.welcome{left:0;top:883px;width:1200px;height:226px;background:var(--blue-dark);text-align:center;color:#fff}
.welcome h2{position:absolute;left:0;width:1200px;top:10px;font-family:Pacifico,cursive;font-weight:400;font-size:36px}
.welcome p{position:absolute;left:160px;width:880px;top:80px;font-size:16px;line-height:20px}
.welcome .more{left:466px;top:154px;width:268px;height:51px;background:var(--pink);font-family:Oswald,sans-serif;font-size:23px;line-height:51px;box-shadow:0 3px 0 #a80c50}
.zigzag{left:0;top:1101px;width:1200px;height:10px;background:linear-gradient(135deg,var(--grey-light) 25%,transparent 25%) 0 0/10px 10px,linear-gradient(225deg,var(--grey-light) 25%,transparent 25%) 0 0/10px 10px}
.services{left:0;top:1109px;width:1200px;height:468px;background:var(--grey-light)}
.services h2{position:absolute;left:0;width:1200px;top:26px;text-align:center;font-family:Pacifico,cursive;font-weight:400;font-size:38px;color:var(--blue)}
.card{top:101px;width:169px;height:297px;background:#fff;border:2px solid #d4d4d6;border-radius:6px;text-align:center}
.card h3{position:absolute;left:0;width:165px;top:12px;font-family:Oswald,sans-serif;font-weight:400;font-size:19px;color:#222;white-space:nowrap}
.card .photo{left:25px;top:54px;width:112px;height:112px;border-radius:50%;border:3px solid #ddd}
.card p{position:absolute;left:10px;width:145px;top:172px;font-size:9.5px;line-height:15px;color:#999}
.card .btn{left:22px;top:250px;width:121px;height:28px;background:var(--pink);color:#fff;font-family:Oswald,sans-serif;font-size:17px;line-height:28px}
.testimonials{left:0;top:1577px;width:1200px;height:271px;background:#fff}
.testimonials h2{position:absolute;left:73px;top:45px;font-family:Montserrat,sans-serif;font-weight:600;font-size:34px;color:var(--blue)}
.quote{top:116px;width:345px;height:150px}
.quote .mark{left:0;top:-8px;font-family:Georgia,serif;font-size:60px;color:#999;line-height:60px}
.quote p{position:absolute;left:40px;width:290px;top:4px;font-size:16.5px;line-height:18px;color:#333}
.quote .close{font-family:Georgia,serif;font-size:30px;color:#999;font-weight:700}
.quote .name{left:40px;top:111px;font-family:Montserrat,sans-serif;font-weight:600;font-size:19px;letter-spacing:.5px}
.divider{top:112px;width:1px;height:150px;background:#dcdcdc}
.callout{left:0;top:1848px;width:1200px;height:136px;background:var(--grey-panel)}
.callout .head{left:69px;top:37px;font-family:"Archivo Black",sans-serif;font-size:39px;color:#2b2b2b;line-height:46px;white-space:nowrap}
.callout .sub{left:69px;top:82px;font-family:Montserrat,sans-serif;font-weight:700;font-size:18px;color:var(--blue);white-space:nowrap}
.callout .call{left:527px;top:41px;font-family:Montserrat,sans-serif;font-weight:600;font-size:20px;color:#999}
.callout .num{left:527px;top:64px;font-family:Montserrat,sans-serif;font-weight:600;font-size:35px;color:var(--blue)}
.callout .allday{left:860px;top:38px;font-family:Montserrat,sans-serif;font-weight:700;font-size:52px;color:#a3a3a3}
.callout .chat{left:995px;top:48px;font-family:Montserrat,sans-serif;font-weight:600;font-size:17px;line-height:21px;color:#555}
.footer{left:0;top:1984px;width:1200px;height:282px;background:var(--footer);color:#fff}
.footer h4{position:absolute;font-family:Montserrat,sans-serif;font-weight:700;font-size:16px}
.footer .input{left:78px;width:227px;height:32px;background:var(--field);font-size:15px;font-style:italic;padding:6px 4px;color:#eee}
.footer .send{left:78px;top:234px;width:78px;height:26px;background:var(--blue);font-size:13px;font-weight:600;text-align:center;line-height:26px}
.links{left:340px;top:62px;width:800px;font-size:17px;line-height:37.5px;color:#eee;white-space:nowrap}
.links .sep{margin:0 11px}
.links .current{color:var(--blue);text-decoration:underline}
.copyright{left:0;top:2266px;width:1200px;height:48px;background:var(--footer-deep);color:#fff;font-size:15px;line-height:48px;padding-left:77px}
</style>
</head>
<body>

<header class="topbar">
  <div class="util">About &nbsp;|&nbsp; Contact</div>
  <div class="social" style="left:229px"></div>
  <div class="social" style="left:262px"></div>
  <div class="social" style="left:295px"></div>
  <div class="phone">
    <svg width="12" height="20" viewBox="0 0 12 20"><rect x="1" y="1" width="10" height="18" rx="2" fill="none" stroke="#fff" stroke-width="2"/><rect x="3" y="4" width="6" height="9" fill="#fff"/></svg>
    07 5550 1842
  </div>
  <div class="schedule">Schedule a Job</div>
</header>

<header class="masthead">
  <div class="brand"><span class="dot"></span><span class="name">BrightLane Washing</span></div>
  <nav class="nav">
    <span class="active">Home</span><span class="sep">|</span>
    <span>Services</span><span class="sep">|</span>
    <span>Commercial</span><span class="sep">|</span>
    <span>Referral Program</span><span class="sep">|</span>
    <span>Blog</span><span class="sep">|</span>
    <span>Testimonials</span><span class="sep">|</span>
    <span>Links</span>
  </nav>
</header>

<section class="hero" role="img" aria-label="Cleaner mopping a bright tiled floor beside a mop bucket in a sunny living room">
  <div class="lead">6 reasons to choose</div>
  <div class="title">BRIGHTLANE</div>
  <div class="reasons">
    <div class="reason">Reputation</div>
    <div class="reason">Experiance</div>
    <div class="reason">Education &amp; Certification</div>
    <div class="reason">Advance Cleaning System</div>
    <div class="reason">1st Class Customer service</div>
    <div class="reason">100% Money back Guarantee</div>
  </div>
  <div class="cta">Get Started</div>
  <div class="ribbon">
    <div class="small">over</div>
    <div class="big">25</div>
    <div class="tiny">year of service quality, &amp; trust</div>
  </div>
</section>

<section class="signup">
  <h2>Sign Up for our new exclusive internet ofers and save $$$</h2>
  <div class="field">Please Enter your email</div>
  <div class="submit">Submit
    <svg width="24" height="24" viewBox="0 0 24 24"><circle cx="12" cy="12" r="10" fill="none" stroke="#fff" stroke-width="2"/><path d="M7 12h9M12 8l4 4-4 4" fill="none" stroke="#fff" stroke-width="2"/></svg>
  </div>
</section>

<section class="welcome">
  <h2>Welcome to my BrightLane..!</h2>
  <p>BrightLane Washing is a professional, full-service carpet, floor, fabric care company serving the North Queensland areas including Cairns, Tablelands, Port Douglas and Mission Beach. BrightLane Carpet Cleaning has been in business since 1996.</p>
  <div class="more">LEARN MORE ABOUT US</div>
</section>
<div class="zigzag"></div>

<section class="services">
  <h2>Our Services</h2>
  <div class="card" style="left:73px">
    <h3>Carpet Cleaning</h3>
    <div class="photo" role="img" aria-label="Carpet cleaning wand on carpet" style="background:radial-gradient(#c9c3bd,#8e857d)"></div>
    <p>Hot water extraction lifts deep dirt, stains and allergens from every fibre, leaving carpets soft and fresh again.</p>
    <div class="btn">More</div>
  </div>
  <div class="card" style="left:252px">
    <h3>Tile &amp; Grout</h3>
    <div class="photo" role="img" aria-label="Tiled floor being scrubbed" style="background:radial-gradient(#b7b9bf,#6f7683)"></div>
    <p>Pressure cleaning clears grime from tiles and grout lines, then a clear seal keeps floors bright for longer.</p>
    <div class="btn">More</div>
  </div>
  <div class="card" style="left:431px">
    <h3>Rug Cleaning</h3>
    <div class="photo" role="img" aria-label="Patterned rug close up" style="background:radial-gradient(#d8cbb3,#8a6f55)"></div>
    <p>Gentle washing suited to wool, silk and synthetic rugs, with careful drying so colours stay rich and true.</p>
    <div class="btn">More</div>
  </div>
  <div class="card" style="left:610px">
    <h3>Water Damage</h3>
    <div class="photo" role="img" aria-label="Flooded room with water" style="background:radial-gradient(#f5c9a0,#e06a1d)"></div>
    <p>Fast response after floods and leaks, with extraction, drying and moisture checks to protect your home or business.</p>
    <div class="btn">More</div>
  </div>
  <div class="card" style="left:789px">
    <h3>UpHolstery Cleaning</h3>
    <div class="photo" role="img" aria-label="Upholstery cleaning tool on a sofa" style="background:radial-gradient(#cfc2b0,#8f7d68)"></div>
    <p>Sofas, chairs and curtains are cleaned on site with fabric safe methods that remove marks and odours.</p>
    <div class="btn">More</div>
  </div>
  <div class="card" style="left:968px">
    <h3>Pest Management</h3>
    <div class="photo" role="img" aria-label="No pests warning sign" style="background:radial-gradient(#fff 55%,#d91f26 57%)"></div>
    <p>Safe, targeted treatments for ants, roaches, spiders and more, keeping your family and pets protected all year.</p>
    <div class="btn">More</div>
  </div>
</section>

<section class="testimonials">
  <h2>Client Testimonials</h2>
  <div class="quote" style="left:70px">
    <div class="mark">&ldquo;</div>
    <p>Lorem Ipsum is simply dummy text of the printing and typesetting industry. Lorem Ipsum has been the industry's standard dummy text ever since the 1500s, <span class="close">&rdquo;</span></p>
    <div class="name">Name - Designation</div>
  </div>
  <div class="divider" style="left:418px"></div>
  <div class="quote" style="left:437px">
    <div class="mark">&ldquo;</div>
    <p>Lorem Ipsum is simply dummy text of the printing and typesetting industry. Lorem Ipsum has been the industry's standard dummy text ever since the 1500s, <span class="close">&rdquo;</span></p>
    <div class="name">Name - Designation</div>
  </div>
  <div class="divider" style="left:774px"></div>
  <div class="quote" style="left:792px">
    <div class="mark">&ldquo;</div>
    <p>Lorem Ipsum is simply dummy text of the printing and typesetting industry. Lorem Ipsum has been the industry's standard dummy text ever since the 1500s, <span class="close">&rdquo;</span></p>
    <div class="name">Name - Designation</div>
  </div>
</section>

<section class="callout">
  <div class="head">Need clean home?</div>
  <div class="sub">GET CLEANING SERVICES YOU CAN TRUST</div>
  <div class="call">Feel Free to call us:</div>
  <div class="num">0400 555 219</div>
  <div class="allday">24/7</div>
  <div class="chat">ONLINE<br>SUPPORT CHAT</div>
</section>

<footer class="footer">
  <h4 style="left:78px;top:32px">Quick Inquiry</h4>
  <div class="input" style="top:69px">Name</div>
  <div class="input" style="top:106px">Email</div>
  <div class="input" style="top:147px;height:80px">Message</div>
  <div class="send">Submit</div>
  <h4 style="left:340px;top:32px">Quick Links</h4>
  <div class="links">
    Flood Damage<span class="sep">|</span>Carpet Cleaning<span class="sep">|</span>Upholstery Cleaning<span class="sep">|</span>Water Damage Specialist<span class="sep">|</span><br>
    Pest Control<span class="sep">|</span>Rug Cleaning<span class="sep">|</span>Leather Cleaning<span class="sep">|</span>Tile and Grout Cleaning<span class="sep">|</span>Natural<br>
    Stone Cleaning<span class="sep">|</span>Urine Damage Treatment<span class="sep">|</span>Pressure Cleaning<span class="sep">|</span>Auto and Marine<span class="sep">|</span><br>
    Fire and Smoke Restoration<span class="sep">|</span>Fabric Protection<span class="sep">|</span>Mould Cleaning<span class="sep">|</span>Trauma Cleaning<span class="sep">|</span><br>
    12 Step carpet cleaning<span class="sep">|</span><span class="current">Home</span>
  </div>
</footer>
<div class="copyright">copyrights @ 2014, brightlanewashing.com.au</div>

</body>
</html>
```